Flyer design for the Harvest Lantern Summit 2019 (HALSUM)

Design a flyer for our annual conference with basic information about the conference: conference logo and year, Conference name: Harvest Lantern Summit Location: Talbot Community Center (Downtown Portland)482 Wexley Street, Portland, ME 04109, Date: August 8th, 9th, 10th and 11th, 2019Start time 7:00PMI would like the following three words added to the flyer. These words describe the vision of the conference: Prophetic, Fire, Overflow,

Contact info:
Website: www.vostel.org
Phone: 207 555 3184
Email: contact@meadowcrest.org

Target Market(s)

Young adults living in the United States

Industry/Entity Type

Religious

Font styles to use
Sans Serif

Colors

Designer to choose colors to be used in the design.

Requirements
Must have
• HALSUM must logo standout, the reader should be able to take a quick look and find key info,
Should not have
• Cross image, church image

```html
<!DOCTYPE html>
<html lang="en">
<head>
<meta charset="utf-8">
<title>Harvest Lantern Summit 2019 – Flyer</title>
<link rel="stylesheet" href="https://fonts.googleapis.com/css2?family=Montserrat:wght@500;600;700;800&family=Oswald:wght@400;500;600&display=swap">
<style>
  :root {
    --bg: #e9e9e8;
    --orange: #ef8a1c;
    --blue: #1f6fb8;
    --blue-dark: #195f9f;
    --ink: #111114;
    --white: #ffffff;
    --grey-ring: #8d8d90;
    --haze-1: #7b7fa6;
    --haze-2: #3b3a55;
    --panel: #eeeeef;
  }
  * { margin: 0; padding: 0; box-sizing: border-box; }
  html, body { width: 1200px; height: 800px; overflow: hidden; background: var(--bg); }
  .flyer {
    position: absolute; left: 330px; top: 20px; width: 540px; height: 760px;
    background: var(--panel); overflow: hidden;
    box-shadow: 0 4px 14px rgba(0,0,0,.18);
    font-family: "Montserrat", sans-serif;
  }
  .hero-photo {
    position: absolute; left: 0; top: 0; width: 540px; height: 460px;
    background:
      linear-gradient(180deg, rgba(0,0,0,0) 35%, rgba(10,10,14,.85) 80%),
      linear-gradient(200deg, #a9acd0 0%, var(--haze-1) 30%, var(--haze-2) 60%, var(--ink) 100%);
  }
  .orange-band { position: absolute; left: 0; top: 440px; width: 540px; height: 24px; background: var(--orange); }
  .info-photo {
    position: absolute; left: 0; top: 464px; width: 540px; height: 216px;
    background: linear-gradient(180deg, #d7d7d9 0%, #f3f3f4 45%, #e2e2e4 100%);
  }
  .logo { position: absolute; right: 36px; top: 40px; text-align: center; }
  .logo-name { font-weight: 700; font-size: 42px; color: var(--blue); letter-spacing: 1px; line-height: 1; }
  .logo-year {
    margin-top: 4px; font-weight: 600; font-size: 17px; color: var(--orange); letter-spacing: 8px;
    border-top: 2px solid var(--orange); padding-top: 2px;
  }
  .title { position: absolute; left: 40px; top: 160px; color: var(--white); line-height: 1.02; }
  .title-line { font-weight: 700; font-size: 50px; letter-spacing: 0.5px; }
  .title-accent { color: var(--orange); font-weight: 800; }
  .title-sub { font-weight: 600; font-size: 44px; }
  .title-year { margin-top: 10px; font-weight: 700; font-size: 32px; letter-spacing: 4px; display: flex; align-items: center; gap: 14px; }
  .title-year::before, .title-year::after { content: ""; width: 34px; height: 3px; background: var(--white); }
  .start-badge {
    position: absolute; left: 352px; top: 355px; width: 176px; height: 176px; border-radius: 50%;
    background: var(--orange); border: 10px solid var(--grey-ring);
    display: flex; flex-direction: column; align-items: center; justify-content: center;
    color: var(--white); text-align: center; line-height: 1.1;
  }
  .start-label { font-weight: 600; font-size: 26px; }
  .start-time { font-weight: 800; font-size: 32px; margin-top: 6px; }
  .start-time small { font-size: 20px; font-weight: 600; }
  .date-block { position: absolute; left: 34px; top: 528px; }
  .month { font-family: "Oswald", sans-serif; font-weight: 500; font-size: 38px; color: var(--blue); line-height: 1; }
  .year-tag {
    margin-top: 4px; display: inline-block; background: var(--orange); color: var(--white);
    font-weight: 700; font-size: 24px; letter-spacing: 4px; padding: 1px 12px;
  }
  .date-divider { position: absolute; left: 178px; top: 524px; width: 3px; height: 106px; background: var(--blue); }
  .date-details { position: absolute; left: 196px; top: 520px; font-family: "Oswald", sans-serif; }
  .days { font-size: 31px; color: var(--orange); font-weight: 500; padding-bottom: 6px; border-bottom: 2px solid var(--blue); }
  .vision { font-size: 26px; color: var(--blue); font-weight: 500; margin-top: 8px; letter-spacing: 0.5px; }
  .venue-bar {
    position: absolute; left: 0; top: 680px; width: 540px; height: 80px; background: var(--blue);
    display: flex; align-items: center; color: var(--white); font-size: 14px; font-weight: 600; line-height: 1.3;
  }
  .venue-bar::before {
    content: ""; position: absolute; left: 256px; top: -10px;
    border-left: 10px solid transparent; border-right: 10px solid transparent; border-bottom: 10px solid var(--blue);
  }
  .venue-name { padding-left: 34px; width: 280px; }
  .venue-name span { font-weight: 500; }
  .venue-sep { width: 1px; height: 40px; background: var(--white); margin-right: 20px; }
  .venue-address { font-weight: 600; }
</style>
</head>
<body>
  <main class="flyer">
    <div class="hero-photo" role="img" aria-label="Crowd of young worshippers with raised hands silhouetted against hazy stage lights"></div>
    <div class="orange-band"></div>
    <div class="info-photo" role="img" aria-label="Faint light-grey photo of raised hands"></div>

    <div class="logo">
      <div class="logo-name">HALSUM</div>
      <div class="logo-year">2019</div>
    </div>

    <h1 class="title">
      <div class="title-line">HARVEST</div>
      <div class="title-line title-accent">LANTERN</div>
      <div class="title-sub">Summit</div>
      <div class="title-year">2019</div>
    </h1>

    <div class="start-badge">
      <div class="start-label">START<br>TIME</div>
      <div class="start-time">7:00 <small>PM</small></div>
    </div>

    <div class="date-block">
      <div class="month">AUGUST</div>
      <div class="year-tag">2019</div>
    </div>
    <div class="date-divider"></div>
    <div class="date-details">
      <div class="days">8TH, 9TH, 10TH AND 11TH</div>
      <div class="vision">PROPHETIC • FIRE • OVERFLOW</div>
    </div>

    <footer class="venue-bar">
      <div class="venue-name">Talbot Community Center<br><span>(Downtown Portland)</span></div>
      <div class="venue-sep"></div>
      <div class="venue-address">482 Wexley Street,<br>Portland, ME 04109</div>
    </footer>
  </main>
</body>
</html>
```